Brevak label design

Redesign cafe range label for lightly carbonated fruit sodas.
Existing label has not worked in the market place and needs to appeal to 18-40 year olds with an active healthy lifestyle.

Product will remain in current 330ml glass bottle and flavour profile will include current range, sparkling water. It is preferred to maintain a body label only but will consider neck label as well. No over cap concepts will be considered..

Attached final shows brand progress. It has lost its way and needs reinvigorating.

Reason: I have extended the deadline to get proper feed back from others on the designs. Thank you all for your submissions so far. Ted

```html
<!DOCTYPE html>
<html lang="en">
<head>
<meta charset="utf-8">
<title>Brevak label</title>
<link rel="stylesheet" href="https://fonts.googleapis.com/css2?family=Almendra:wght@400;700&display=swap">
<style>
  :root {
    --label-yellow: #f7d819;
    --ink: #1c1a14;
    --badge-rim: #141114;
    --badge-ring: #ffffff;
    --badge-core: #3a1f3e;
    --badge-edge: #0f0c10;
    --brand-orange: #f7a024;
    --band-magenta: #b51fb5;
  }
  html, body {
    margin: 0;
    padding: 0;
    width: 1200px;
    height: 999px;
    overflow: hidden;
    background: var(--label-yellow);
  }
  .label {
    position: relative;
    width: 1200px;
    height: 999px;
    background: var(--label-yellow);
    font-family: "Almendra", serif;
    color: var(--ink);
  }
  .brand-badge {
    position: absolute;
    left: 453px;
    top: 285px;
    width: 296px;
    height: 296px;
    box-sizing: border-box;
    border-radius: 50%;
    border: 6px solid var(--badge-rim);
    box-shadow: inset 0 0 0 7px var(--badge-ring);
    background: radial-gradient(circle at 50% 55%, var(--badge-core) 0%, #24142a 55%, var(--badge-edge) 100%);
    display: flex;
    align-items: center;
    justify-content: center;
  }
  .brand-name {
    font-family: "Almendra", serif;
    font-weight: 700;
    font-size: 84px;
    color: var(--brand-orange);
    line-height: 1;
    margin-top: -6px;
  }
  .volume {
    position: absolute;
    left: 342px;
    top: 542px;
    margin: 0;
    font-size: 27px;
    font-style: italic;
    letter-spacing: 1px;
    line-height: 1.2;
  }
  .tagline {
    position: absolute;
    left: 333px;
    top: 578px;
    margin: 0;
    font-size: 54px;
    font-weight: 700;
    line-height: 1.2;
    white-space: nowrap;
  }
  .carbonation {
    position: absolute;
    left: 676px;
    top: 660px;
    margin: 0;
    font-size: 19px;
    font-style: italic;
    line-height: 1.2;
    white-space: nowrap;
  }
  .accent-band {
    position: absolute;
    left: 0;
    top: 0;
  }
</style>
</head>
<body>
  <main class="label">
    <div class="brand-badge">
      <span class="brand-name">Brevak</span>
    </div>
    <p class="volume">330ml</p>
    <h1 class="tagline">Fresh Tasty Fruit Drink</h1>
    <svg class="accent-band" width="1200" height="999" viewBox="0 0 1200 999" aria-hidden="true">
      <polygon fill="var(--band-magenta)" points="287,682 720,688 915,668 876,700 720,690 322,710"/>
    </svg>
    <p class="carbonation">&ldquo;Lightly Carbonated&rdquo;</p>
  </main>
</body>
</html>
```